Sports hypnotherapist needs electronic letterhead design

Need a simple but classy design for a letterhead that looks good when printed. Its for a hypnotherapist who specialises in elite sport. Should have my company name and address and website details on it. I specialise in footballers.
Should look good electronically and when printed.
Include all contact details as shown in the must haves.

Target Market(s)

Sports people, elite sport.

Industry/Entity Type

Hypnotherapy

Font styles to use
Sans Serif

Colors

Designer to choose colors to be used in the design.

Requirements
Must have
• NEEDS TO BE DESIGNED IN MS WORD
• Logo +
• Blue Heron Hypnotherapists
• 27 Marlowe Close
• Bracknell
• RG41 5PL
• Tel: 07700 900461
• E: blueheroncoaching@mailvale.com
• www: http://www.blue-heron-clinic.co.uk.
• Derek Ashworth
• Clinical hypnotherapist, hypnoanalyst, mental resilience coach, MSc, Dip PHH
Nice to have
• A watermark?
• Plenty of space for the A4 letter
• Prints well.
Should not have
• Too much clutter.
• Too much colour that will be costly to print.

```html
<!DOCTYPE html>
<html lang="en">
<head>
<meta charset="utf-8">
<title>Blue Heron Hypnotherapists – Letterhead</title>
<link rel="stylesheet" href="https://fonts.googleapis.com/css2?family=Montserrat:wght@400;600;700&family=Roboto:wght@300;400;700&display=swap">
<style>
  :root {
    --backdrop: #ececec;
    --paper: #ffffff;
    --ink: #2b2b2b;
    --ink-soft: #555555;
    --accent: #3bb4e8;
    --figure-grey: #9a9a9a;
    --figure-blue: #cfe8f6;
  }
  html, body {
    margin: 0;
    padding: 0;
    width: 1200px;
    height: 1091px;
    overflow: hidden;
    background: var(--backdrop);
  }
  .letterhead {
    position: absolute;
    left: 236px;
    top: 30px;
    width: 728px;
    height: 1030px;
    background: var(--paper);
    box-shadow: 0 2px 10px rgba(0,0,0,0.08);
    font-family: "Roboto", Arial, sans-serif;
    color: var(--ink);
  }
  .brand {
    position: absolute;
    left: 52px;
    top: 46px;
    display: flex;
    align-items: center;
    gap: 10px;
  }
  .brand-dot {
    width: 22px;
    height: 22px;
    border-radius: 50%;
    background: var(--accent);
  }
  .brand-name {
    font-family: "Montserrat", Arial, sans-serif;
    font-weight: 700;
    font-size: 28px;
    color: var(--ink);
    letter-spacing: 0.2px;
  }
  .practitioner {
    position: absolute;
    right: 52px;
    top: 128px;
    text-align: right;
  }
  .practitioner-name {
    font-family: "Montserrat", Arial, sans-serif;
    font-weight: 700;
    font-size: 17px;
    letter-spacing: 2px;
    text-transform: uppercase;
    margin: 0 0 6px;
  }
  .practitioner-title {
    font-family: "Montserrat", Arial, sans-serif;
    font-weight: 600;
    font-size: 11px;
    line-height: 1.45;
    margin: 0;
  }
  .recipient {
    position: absolute;
    left: 52px;
    top: 128px;
    font-family: "Montserrat", Arial, sans-serif;
    font-size: 11px;
    line-height: 1.5;
  }
  .recipient strong { font-weight: 700; }
  .letter-body {
    position: absolute;
    left: 52px;
    top: 230px;
    width: 610px;
    font-size: 10.5px;
    line-height: 1.55;
    color: var(--ink-soft);
  }
  .letter-body p { margin: 0 0 14px; }
  .signature {
    position: absolute;
    left: 52px;
    top: 560px;
    width: 190px;
  }
  .signature-mark { display: block; width: 190px; height: 50px; }
  .signature-rule { border: 0; border-top: 1px solid var(--ink-soft); margin: 4px 0 6px; }
  .signature-role { font-size: 12px; color: var(--ink-soft); }
  .footer-rule {
    position: absolute;
    left: 52px;
    top: 740px;
    width: 470px;
    height: 2px;
    background: var(--accent);
  }
  .footer {
    position: absolute;
    left: 52px;
    top: 758px;
    width: 500px;
    display: flex;
    gap: 34px;
    font-size: 11px;
    line-height: 1.6;
  }
  .footer-label { font-weight: 700; color: var(--ink); }
  .footer-value { color: var(--accent); }
  .footer-address { color: var(--ink); }
  .hero-figure {
    position: absolute;
    right: 40px;
    bottom: 40px;
    width: 170px;
    height: 330px;
  }
</style>
</head>
<body>
  <main class="letterhead">
    <header class="brand">
      <span class="brand-dot"></span>
      <span class="brand-name">Blue Heron</span>
    </header>

    <section class="recipient">
      To<br>
      <strong>Alan Price, CEO, NORTHWAVE STUDIO</strong>
    </section>

    <section class="practitioner">
      <h1 class="practitioner-name">Derek Ashworth</h1>
      <p class="practitioner-title">Clinical hypnotherapist, hypnoanalyst,<br>Mental Resilience Coach, MSc, Dip PHH</p>
    </section>

    <article class="letter-body">
      <p>Lorem ipsum dolor sit amet, an habeo errem euismod pri. Per id tation exerci lucilius. Usu at congue interesset, est explicari moderatius et, id pro esse docendi. Mea ancillae mentitum atomorum ne, eum congue ponderum eu. Ut mei quidam detraxit similique, dissentias omittantur ut mei.</p>
      <p>Cu nec purto accusam, aliquid graecis disputando quo cu, id augue affert nam. Ex quo cibo iuvaret explicari. In postea disputationi mea, meliore recusabo hendrerit ius et, alienum molestie torquatos vel et. Nam virtute recteque inciderint ei. Sed cibo similique quaerendum ut, ex dolorem constituto eos, cu elit elitr ancillae eos. Virtute mentitum invidunt mea te. Qui quis tollit disputando cu, modus melius ne mel.</p>
      <p>Duo oportere petentium in, odio putant placerat usu ad. Vis ut error electram, id placerat singulis postulant his, pri graecis accommodare at. Ut qui ignota inermis partiendo, vis maiestatis abhorreant ei, cu utinam posidonium eam. Mel odio nibh deleniti ei, vel ad quodsi impetus explicari. Te mea facilis recteque, harum munere nostrud ea usu. Alii meis est ne, eos consul mucius forensibus te.</p>
      <p>Cu nec purto accusam, aliquid graecis disputando quo cu, id augue affert nam. Ex quo cibo iuvaret explicari. In postea disputationi mea, meliore recusabo hendrerit ius et, alienum molestie torquatos vel et. Nam virtute recteque inciderint ei. Sed cibo similique quaerendum ut, ex dolorem constituto eos, cu elit elitr ancillae eos. Virtute mentitum invidunt mea te. Qui quis tollit disputando cu, modus melius ne mel.</p>
      <p>Lorem ipsum dolor sit amet, an habeo errem euismod pri. Per id tation exerci lucilius. Usu at congue interesset, est explicari moderatius et, id pro esse docendi. Mea ancillae mentitum atomorum ne, eum congue ponderum eu. Ut</p>
    </article>

    <section class="signature">
      <svg class="signature-mark" role="img" aria-label="Handwritten signature of Derek Ashworth" viewBox="0 0 190 50">
        <rect x="0" y="8" width="190" height="40" rx="4" fill="#f1f1f1"/>
      </svg>
      <hr class="signature-rule">
      <div class="signature-role">your designation</div>
    </section>

    <div class="footer-rule"></div>
    <footer class="footer">
      <div class="footer-address">27 Marlowe Close<br>Bracknell, RG41 5PL</div>
      <div>
        <span class="footer-label">Email:</span> <span class="footer-value">blueheroncoaching@mailvale.com</span><br>
        <span class="footer-label">Web:</span> <span class="footer-value">http://www.blue-heron-clinic.co.uk.</span>
      </div>
      <div><span class="footer-label">Tel:</span> <span class="footer-value">07700 900461</span></div>
    </footer>

    <svg class="hero-figure" role="img" aria-label="Grey silhouette of a standing man with a light blue cape, faint watermark illustration" viewBox="0 0 170 330">
      <defs>
        <linearGradient id="figureTone" x1="0" y1="0" x2="1" y2="1">
          <stop offset="0" stop-color="#b3b3b3"/>
          <stop offset="0.6" stop-color="#9a9a9a"/>
          <stop offset="1" stop-color="#cfe8f6"/>
        </linearGradient>
      </defs>
      <rect x="0" y="0" width="170" height="330" rx="6" fill="url(#figureTone)" opacity="0.55"/>
    </svg>
  </main>
</body>
</html>
```